Website design for learning and development business

I need a logo for my new business based in Australasia. I am a kiwi who is a creative change maker working in the Learning & development space. I design experiential learning opportunities for businesses to grow and nurture their tribes. I take a holistic look at an organisation and analyse what is needed to build a positive culture with a growth mindset woven into their DNA. I would like to see designs that are based on the following word snaps - creative, interesting, tribal, journey, adaptability, engaging, fluid, architectural, bespoke, courageous, challenging .I have the logo (attached) and I Need a startup business website designed. I am a Learning and development professional who is looking at going out on my own and establishing my own business. I would like a website designed that people would go to to check out what I do, how I do, what skills I have and how to contact me. Also room for a blog/articles.

Target Market(s)

Small to medium business

Industry/Entity Type

Self employed training and consultancy company

Number of Pages Required

5+ page

Requirements
Must have
• home page, about page, contact us page, blog page, search for us page
Nice to have
• Testimonials,

```html
<!DOCTYPE html>
<html lang="en">
<head>
<meta charset="utf-8">
<title>TRIBEWAY – Learning &amp; Development Business</title>
<link rel="stylesheet" href="https://fonts.googleapis.com/css2?family=Poppins:wght@400;500;600;700&display=swap">
<style>
:root{
  --blue:#1155a8;
  --blue-deep:#0d4690;
  --blue-band:#2a64ac;
  --orange:#f7931e;
  --ink:#2b2b2b;
  --muted:#6f7780;
  --light:#f3f4f6;
  --grey-band:#f1f1f1;
  --footer:#22262e;
  --footer-cta:#2a2e37;
  --footer-base:#1a1d23;
  --white:#ffffff;
}
*{box-sizing:border-box;margin:0;padding:0}
html,body{width:1200px;height:3866px;overflow:hidden}
body{position:relative;font-family:"Poppins",sans-serif;color:var(--ink);background:var(--white)}
.abs{position:absolute}
section,header,footer{position:absolute;left:0;width:1200px}

/* header */
.site-header{top:0;height:98px;background:var(--white)}
.brand{left:192px;top:34px;font-size:30px;font-weight:700;color:var(--blue);letter-spacing:.5px}
.contact-mini{left:716px;top:14px;display:flex;gap:10px;align-items:center;font-size:11px;line-height:14px;color:#333}
.contact-mini strong{font-weight:600;font-size:12px}
.quote-btn{left:896px;top:14px;width:110px;height:30px;border-radius:15px;background:var(--blue);color:#fff;font-size:10px;font-weight:600;display:flex;align-items:center;justify-content:center}
.main-nav{left:488px;top:57px;width:712px;height:41px;background:var(--blue);border-radius:8px 0 0 0;display:flex;align-items:center;font-size:15px;color:#fff}
.main-nav span{position:absolute;top:10px}
.main-nav .active::after{content:"";position:absolute;left:-2px;right:-2px;top:28px;height:2px;background:#fff}

/* hero */
.hero{top:98px;height:660px}
.hero-photo{left:0;top:0;width:1200px;height:660px;background:linear-gradient(110deg,#3a3a3e 0%,#55565c 30%,#2d3a55 60%,#1b2c52 100%)}
.hero-title{left:597px;top:200px;font-size:37px;line-height:44px;font-weight:600;color:#fff}
.hero-text{left:597px;top:302px;width:420px;font-size:17px;line-height:27px;color:#e8ecf3}
.hero-btn{left:600px;top:377px;width:165px;height:36px;border-radius:18px;background:var(--orange);color:#fff;font-size:13px;font-weight:500;display:flex;align-items:center;justify-content:center}
.hero-arrow{top:236px;width:50px;height:50px;border-radius:50%;border:2px solid #fff;background:var(--blue);display:flex;align-items:center;justify-content:center}

/* welcome */
.welcome{top:700px;height:450px;background:var(--light)}
.welcome h2{position:absolute;left:0;width:1200px;top:126px;text-align:center;font-size:22px;font-weight:600;color:#222}
.welcome h2 em{font-style:normal;color:var(--orange)}
.welcome p{position:absolute;left:270px;width:660px;text-align:center;color:#444}
.learn-btn{left:531px;top:322px;width:137px;height:36px;border-radius:18px;background:#7b7b7d;color:#fff;font-size:12px;font-weight:500;display:flex;align-items:center;justify-content:center}

/* services */
.services{top:1150px;height:570px;background:var(--white)}
.eyebrow{left:0;width:1200px;top:68px;display:flex;justify-content:center;align-items:center;gap:12px;color:var(--blue);font-size:16px}
.eyebrow i{display:block;width:34px;height:2px;background:var(--blue)}
.services h2{position:absolute;left:0;width:1200px;top:96px;text-align:center;font-size:35px;font-weight:600;color:#2a2a2a}
.service-card{width:232px}
.service-card .photo{width:232px;height:212px;box-shadow:0 4px 10px rgba(0,0,0,.12)}
.service-card .cap{position:relative;margin-top:18px;padding-left:12px;border-left:3px solid var(--blue)}
.service-card h3{font-size:14px;font-weight:500;color:#222;line-height:18px}
.service-card p{font-size:11px;color:#555;line-height:15px}
.go{position:absolute;right:4px;top:2px;width:26px;height:26px;border-radius:50%;border:2px solid var(--orange);color:var(--orange);font-size:12px;font-weight:600;display:flex;align-items:center;justify-content:center}

/* features */
.features{top:1720px;height:220px;background:var(--grey-band)}
.feature{top:70px;width:260px;display:flex;gap:14px}
.feature h4{font-size:14px;font-weight:600;color:#222;margin-top:6px}
.feature p{font-size:12px;color:#777;line-height:19px;margin-top:4px}

/* testimonials */
.testimonials{top:1940px;height:436px;background:linear-gradient(90deg,#2c5fa4 0%,#2f66ad 50%,#1f56a0 100%)}
.testimonials h2{position:absolute;left:0;width:1200px;top:64px;text-align:center;font-size:28px;font-weight:700;color:#fff}
.quote-card{top:134px;width:350px;height:115px;background:#fff;padding:24px 20px 0 52px;font-size:11.5px;line-height:20px;color:#555}
.quote-card::after{content:"";position:absolute;left:30px;bottom:-14px;border-left:9px solid transparent;border-right:9px solid transparent;border-top:14px solid #fff}
.quote-mark{position:absolute;left:20px;top:22px;font-size:34px;line-height:30px;font-weight:700;color:var(--blue)}
.author{top:278px;display:flex;align-items:center;gap:14px;color:#fff}
.avatar{width:42px;height:42px;border-radius:50%;background:#d9dfe8;border:2px solid #fff}
.author b{display:block;font-size:11px;font-weight:600}
.author span{font-size:10px}
.dots{left:584px;top:356px;display:flex;gap:4px}
.dots i{width:7px;height:7px;border-radius:50%;border:1px solid #fff}
.dots i.on{background:var(--orange);border-color:var(--orange)}

/* blog */
.blog{top:2376px;height:520px;background:#fff}
.blog h2{position:absolute;left:0;width:1200px;top:44px;text-align:center;font-size:22px;font-weight:600;color:#333}
.post{top:112px;width:232px;text-align:center}
.post .photo{width:232px;height:241px;position:relative}
.post .num{position:absolute;left:0;top:0;width:48px;height:48px;background:var(--blue);color:#fff;font-size:18px;font-weight:600;display:flex;align-items:center;justify-content:center}
.post h3{margin-top:20px;font-size:15px;font-weight:600;color:#333}
.post p{margin:6px auto 0;width:200px;font-size:11px;line-height:17px;color:#777}
.post .more{margin-top:4px;color:var(--blue);font-size:16px;letter-spacing:2px;line-height:14px}

/* contact */
.contact{top:2896px;height:555px;background:#f4f4f5}
.contact h2{position:absolute;left:62px;top:92px;font-size:22px;font-weight:700;color:#2a2a2a}
.contact .sub{left:62px;top:130px;font-size:8px;letter-spacing:1.5px;color:#aab}
.field{background:#fff;border:1px solid #e6e6e8;font-size:7.5px;letter-spacing:1px;color:#999;padding:11px 18px}
.send-btn{left:62px;top:441px;width:102px;height:25px;border-radius:13px;background:var(--orange);color:#fff;font-size:7px;letter-spacing:.8px;font-weight:500;display:flex;align-items:center;justify-content:center}
.contact-photo{left:600px;top:0;width:600px;height:555px;background:linear-gradient(135deg,#e9e8e2 0%,#c9cfc6 40%,#b56a50 70%,#d9d4ca 100%)}

/* footer */
.cta-bar{top:3451px;height:84px;background:var(--footer-cta)}
.cta-bar p{position:absolute;left:248px;top:29px;font-size:17px;color:#fff}
.cta-bar p b{font-weight:600}
.cta-btn{left:841px;top:25px;width:137px;height:33px;background:var(--blue);color:#fff;font-size:10.5px;font-weight:600;display:flex;align-items:center;justify-content:center}
.site-footer{top:3535px;height:265px;background:var(--footer);color:#fff}
.foot-brand{left:178px;top:48px;font-size:29px;font-weight:600;color:#fff}
.foot-about{left:180px;top:120px;width:200px;font-size:10px;line-height:17px;color:#d5d7dc}
.vline{top:46px;width:1px;height:150px;background:#3a3f49}
.foot-col h5{font-size:15px;font-weight:400;color:#fff}
.foot-col h5::before{content:"";display:block;width:26px;height:2px;background:var(--orange);margin-bottom:16px}
.foot-col ul{list-style:none;margin-top:22px;font-size:11px;color:#d5d7dc;line-height:21px}
.foot-col li{display:flex;gap:8px;align-items:flex-start;margin-bottom:8px;line-height:15px}
.social{display:flex;gap:5px;margin-top:12px}
.social i{width:20px;height:20px;border-radius:50%;background:var(--blue);display:block}
.news{left:871px;top:200px;width:147px;height:28px;background:#fff;font-size:9px;color:#999;padding:6px 10px}
.news-btn{left:990px;top:200px;width:28px;height:28px;background:var(--blue);display:flex;align-items:center;justify-content:center}
.base{top:3800px;height:66px;background:var(--footer-base);color:#c8cad0;font-size:10px}
</style>
</head>
<body>

<header class="site-header">
  <div class="abs brand">TRIBEWAY</div>
  <div class="abs contact-mini">
    <svg width="22" height="22" viewBox="0 0 24 24"><path d="M6.6 10.8a15.1 15.1 0 0 0 6.6 6.6l2.2-2.2c.3-.3.7-.4 1-.2 1.1.4 2.3.6 3.6.6.6 0 1 .4 1 1V20c0 .6-.4 1-1 1A17 17 0 0 1 3 4c0-.6.4-1 1-1h3.5c.6 0 1 .4 1 1 0 1.2.2 2.4.6 3.6.1.3 0 .7-.2 1z" fill="#1155a8"/></svg>
    <div><strong>0400 555 018 22</strong><br>hello@tribeway.example</div>
  </div>
  <div class="abs quote-btn">GET A QUOTE</div>
  <nav class="abs main-nav">
    <span class="active" style="left:56px">HOME</span>
    <span style="left:153px">ABOUT</span>
    <span style="left:258px">BLOG</span>
    <span style="left:352px">CONTACT US</span>
    <svg style="position:absolute;left:494px;top:11px" width="20" height="20" viewBox="0 0 20 20"><circle cx="8" cy="8" r="6" fill="none" stroke="#fff" stroke-width="2"/><line x1="12.5" y1="12.5" x2="18" y2="18" stroke="#fff" stroke-width="2"/></svg>
  </nav>
</header>

<section class="welcome">
  <h2>WELCOME TO <em>TRIBEWAY</em></h2>
  <p style="top:170px;font-size:13px;line-height:24px">Lorem ipsum dolor sit amet, consectetur adipiscing elit. Nam commodo ligula ac felis dapibus faucibus. Nulla vitae metus vitae justo lobortis rhoncus.</p>
  <p style="top:230px;font-size:11.5px;line-height:24px;color:#555">Lorem ipsum dolor sit amet, consectetur adipiscing elit. Nam commodo ligula ac felis dapibus faucibus. Nulla vitae metus vitae justo lobortis rhoncus. Ut et sodales diam. Proin ultricies libero eget lectus suscipit efficitur. Suspendisse vel turpis libero. Donec viverra feugiat tristique.</p>
  <div class="abs learn-btn">LEARN MORE</div>
</section>

<section class="hero">
  <div class="abs hero-photo" role="img" aria-label="Close-up of a hand placing wooden building blocks overlaid with a network of wireframe cubes"></div>
  <svg class="abs" style="left:0;top:0" width="1200" height="660" viewBox="0 0 1200 660">
    <path d="M0 540 Q600 760 1200 530 L1200 660 L0 660 Z" fill="#f3f4f6"/>
    <path d="M0 540 Q600 760 1200 530" fill="none" stroke="#1155a8" stroke-width="6"/>
    <rect x="590" y="558" width="16" height="24" rx="8" fill="none" stroke="#fff" stroke-width="2"/>
    <line x1="598" y1="564" x2="598" y2="570" stroke="#fff" stroke-width="2"/>
    <path d="M598 584 v10 M594 590 l4 4 4-4" stroke="#fff" stroke-width="1.5" fill="none"/>
  </svg>
  <div class="abs hero-title">LEARNING &amp;<br>DEVELOPMENT BUSINESS</div>
  <div class="abs hero-text">Lorem ipsum dolor sit amet, consectetur adipiscing elit nunc at augue lacus.</div>
  <div class="abs hero-btn">CONTACT US NOW</div>
  <div class="abs hero-arrow" style="left:40px"><svg width="16" height="16" viewBox="0 0 16 16"><path d="M10 2 L4 8 L10 14" stroke="#fff" stroke-width="3" fill="none"/></svg></div>
  <div class="abs hero-arrow" style="left:1108px"><svg width="16" height="16" viewBox="0 0 16 16"><path d="M6 2 L12 8 L6 14" stroke="#fff" stroke-width="3" fill="none"/></svg></div>
</section>

<section class="services">
  <div class="abs eyebrow"><i></i>Our Services<i></i></div>
  <h2>What We Do</h2>
  <div class="abs service-card" style="left:193px;top:186px">
    <div class="photo" role="img" aria-label="Two colleagues working together at a computer" style="background:linear-gradient(135deg,#dfe3e8,#9aa4ad 60%,#6d6a66)"></div>
    <div class="cap"><h3>Busness Development</h3><p>Lorem ipsum dolor sit</p><span class="go">»</span></div>
  </div>
  <div class="abs service-card" style="left:484px;top:217px">
    <div class="photo" role="img" aria-label="Smiling team members in a casual office meeting" style="background:linear-gradient(135deg,#eceef0,#b9bfc4 55%,#5b6470)"></div>
    <div class="cap"><h3>Busness Development</h3><p>Lorem ipsum dolor sit</p><span class="go">»</span></div>
  </div>
  <div class="abs service-card" style="left:774px;top:186px">
    <div class="photo" role="img" aria-label="Businesswoman reviewing documents at a desk" style="background:linear-gradient(135deg,#c9d2b0,#8c9580 50%,#3e4548)"></div>
    <div class="cap"><h3>Busness Development</h3><p>Lorem ipsum dolor sit</p><span class="go">»</span></div>
  </div>
</section>

<section class="features">
  <div class="abs feature" style="left:190px">
    <svg width="42" height="42" viewBox="0 0 42 42" fill="none" stroke="#555" stroke-width="1.6"><circle cx="22" cy="21" r="15"/><circle cx="22" cy="21" r="9"/><circle cx="22" cy="21" r="3"/><path d="M22 21 L4 10 M4 10 l1 6 M4 10 l6 0"/></svg>
    <div><h4>Investing</h4><p>Internal accounting &amp; sales data, in addition to external market</p></div>
  </div>
  <div class="abs feature" style="left:472px">
    <svg width="42" height="42" viewBox="0 0 42 42" fill="none" stroke="#555" stroke-width="1.6"><rect x="3" y="12" width="36" height="24" rx="2"/><path d="M15 12 V7 h12 v5 M3 22 h36"/><rect x="18" y="19" width="6" height="6"/></svg>
    <div><h4>Finance</h4><p>Internal accounting &amp; sales data, in addition to external market</p></div>
  </div>
  <div class="abs feature" style="left:754px">
    <svg width="42" height="42" viewBox="0 0 42 42" fill="none" stroke="#555" stroke-width="1.6"><path d="M4 24 L14 14 L22 20 L30 12 L38 20 L24 34 Z"/><path d="M14 26 l6 6 M18 22 l6 6"/><path d="M8 10 l6 -6 M30 4 l6 6"/></svg>
    <div><h4>Consulting</h4><p>Internal accounting &amp; sales data, in addition to external market</p></div>
  </div>
</section>

<section class="testimonials" role="img" aria-label="Blue-tinted background of a smiling client shaking hands">
  <h2>WHAT CLIENT SAY</h2>
  <div class="abs quote-card" style="left:234px"><span class="quote-mark">“</span>The heights by great men reached kept attoine by sudden flight, but the while companion slept were tooiling upward in the night.</div>
  <div class="abs quote-card" style="left:618px"><span class="quote-mark">“</span>The heights by great men reached kept attoine by sudden flight, but the while companion slept were tooiling upward in the night.</div>
  <div class="abs author" style="left:252px"><div class="avatar" role="img" aria-label="Client portrait"></div><div><b>MARA QUILL</b><span>Senior UI/UX Designer</span></div></div>
  <div class="abs author" style="left:636px"><div class="avatar" role="img" aria-label="Client portrait"></div><div><b>THEO BRANDT</b><span>Senior UI/UX Designer</span></div></div>
  <div class="abs dots"><i class="on"></i><i></i><i></i></div>
</section>

<section class="blog">
  <h2>Latest Blog</h2>
  <article class="abs post" style="left:234px">
    <div class="photo" role="img" aria-label="Glass skyscrapers seen from below" style="background:linear-gradient(160deg,#bcd6ee,#2f6fb5 55%,#123c73)"><span class="num">01</span></div>
    <h3>Investing in shares</h3><p>Internal accounting &amp; sales data, in the addition to external market</p><div class="more">...</div>
  </article>
  <article class="abs post" style="left:484px">
    <div class="photo" role="img" aria-label="Glasses and pen resting on a printed bar chart" style="background:linear-gradient(160deg,#e7eef6,#8fc0ea 55%,#3d8fd6)"><span class="num">02</span></div>
    <h3>Investing in shares</h3><p>Internal accounting &amp; sales data, in the addition to external market</p><div class="more">...</div>
  </article>
  <article class="abs post" style="left:734px">
    <div class="photo" role="img" aria-label="Office towers against a blue sky" style="background:linear-gradient(160deg,#dce9f6,#4a82c0 55%,#1b3f73)"><span class="num">03</span></div>
    <h3>Investing in shares</h3><p>Internal accounting &amp; sales data, in the addition to external market</p><div class="more">...</div>
  </article>
</section>

<section class="contact">
  <h2>GET IN TOUCH WITH US</h2>
  <div class="abs sub">FEEL FREE TO CONTACT US</div>
  <div class="abs field" style="left:62px;top:178px;width:229px;height:32px">YOUR NAME</div>
  <div class="abs field" style="left:308px;top:178px;width:229px;height:32px">EMAIL ADDRESS</div>
  <div class="abs field" style="left:62px;top:228px;width:474px;height:32px">SUBJECT</div>
  <div class="abs field" style="left:62px;top:278px;width:474px;height:138px">YOUR MESSAGE</div>
  <div class="abs send-btn">SEND MESSAGE</div>
  <div class="abs contact-photo" role="img" aria-label="Smiling man in a checked shirt working at a desk under a lamp"></div>
</section>

<div class="abs cta-bar" style="left:0;width:1200px">
  <p>Have any question or <b>need any business consultation?</b></p>
  <div class="abs cta-btn">CONTACT US NOW!!</div>
</div>

<footer class="site-footer">
  <div class="abs foot-brand">TRIBEWAY</div>
  <p class="abs foot-about">Lorem ipsum dolor sit amet, consectetur adipiscing elit. Nullam sollicitudin tempor sem vitae pretium. Fusce ultricies mollis purus non rutrum.</p>
  <div class="abs vline" style="left:392px"></div>
  <div class="abs vline" style="left:560px"></div>
  <div class="abs vline" style="left:815px"></div>
  <div class="abs foot-col" style="left:446px;top:46px">
    <h5>Site Links</h5>
    <ul style="margin-top:24px;line-height:21px"><li style="margin:0;line-height:21px">Home</li><li style="margin:0;line-height:21px">About Us</li><li style="margin:0;line-height:21px">Blog</li><li style="margin:0;line-height:21px">Contact Us</li><li style="margin:0;line-height:21px">Get a quote</li></ul>
  </div>
  <div class="abs foot-col" style="left:603px;top:46px;width:190px">
    <h5>Contact Us</h5>
    <ul>
      <li><svg width="14" height="14" viewBox="0 0 24 24"><path d="M6.6 10.8a15.1 15.1 0 0 0 6.6 6.6l2.2-2.2c.3-.3.7-.4 1-.2 1.1.4 2.3.6 3.6.6.6 0 1 .4 1 1V20c0 .6-.4 1-1 1A17 17 0 0 1 3 4c0-.6.4-1 1-1h3.5c.6 0 1 .4 1 1 0 1.2.2 2.4.6 3.6.1.3 0 .7-.2 1z" fill="none" stroke="#ccc" stroke-width="1.6"/></svg>Phone: 0400 555 0182</li>
      <li><svg width="14" height="14" viewBox="0 0 24 24"><path d="M12 22s7-7 7-12a7 7 0 0 0-14 0c0 5 7 12 7 12z" fill="none" stroke="#ccc" stroke-width="1.6"/><circle cx="12" cy="10" r="2.5" fill="none" stroke="#ccc" stroke-width="1.6"/></svg>Address: 48 Harbour Lane, Level 2, Wellington, NZ</li>
      <li><svg width="14" height="14" viewBox="0 0 24 24"><rect x="3" y="6" width="18" height="13" fill="none" stroke="#ccc" stroke-width="1.6"/><path d="M3 6 l9 7 9-7" fill="none" stroke="#ccc" stroke-width="1.6"/></svg>Email: hello@tribeway.example</li>
    </ul>
  </div>
  <div class="abs foot-col" style="left:871px;top:46px">
    <h5>Get Connected</h5>
    <div class="social"><i></i><i></i><i></i></div>
  </div>
  <div class="abs foot-col" style="left:871px;top:149px"><h5>Newsletter</h5></div>
  <div class="abs news">Email...</div>
  <div class="abs news-btn"><svg width="14" height="14" viewBox="0 0 24 24"><path d="M2 12 L22 3 L15 22 L11 13 Z" fill="#fff"/></svg></div>
</footer>

<div class="abs base" style="left:0;width:1200px">
  <span class="abs" style="left:186px;top:26px">@2021 TRIBEWAY &nbsp;|&nbsp; All Rights Reserved.</span>
  <span class="abs" style="left:827px;top:26px">Terms &amp; Conditions &nbsp;|&nbsp; Privacy Policy</span>
</div>

</body>
</html>
```